2 sided flyer for Insurance Servics

Would like a flyer that talks about who we are, our services, and our process. Attaching relevant information, as well as our Logo and other logos for a few larger insurance carriers that we have access to.

Target Market(s)

Financial Advisors and Insurance Agents

Industry/Entity Type

Finance and Insurance

Colors
0054AA
0677BA
7BADD7
CADEEF
E8F1F8
F0912C
F2A743
F7CA91
FBE8D2
FDF5EE

Requirements
Must have
• Lists, bullet points, pictures, and logos uploaded

```html
<!DOCTYPE html>
<html lang="en">
<head>
<meta charset="utf-8">
<title>Northvale Insurance Network – Two-sided Flyer</title>
<link rel="stylesheet" href="https://fonts.googleapis.com/css2?family=Montserrat:wght@400;500;600;700;800&display=swap">
<style>
:root{
  --navy:#232b70;
  --ink:#2f3445;
  --panel:#e4e8ee;
  --paper:#ffffff;
  --backdrop:#8f8f8f;
  --line:#c9ced8;
}
*{box-sizing:border-box;margin:0;padding:0}
html,body{width:821px;height:1200px;overflow:hidden;background:var(--backdrop);font-family:"Montserrat",sans-serif;color:var(--ink)}
.sheet-row{position:absolute;left:10px;top:323px;width:801px;height:555px}
.page{position:absolute;top:0;width:700px;height:990px;background:var(--paper);transform:scale(.56);transform-origin:0 0;overflow:hidden;box-shadow:0 6px 24px rgba(0,0,0,.35)}
.page--front{left:0}
.page--back{left:409px}

/* shared */
.tab{display:inline-block;background:var(--navy);color:#fff;font-weight:700;font-size:18px;letter-spacing:1px;padding:5px 24px 5px 12px;clip-path:polygon(0 0,86% 0,100% 100%,0 100%)}
.tab--light{background:var(--paper);color:var(--navy)}
p,li{font-size:10.5px;line-height:1.2;letter-spacing:.2px}
b{font-weight:700}
.num{display:inline-block;width:13px;height:13px;background:var(--navy);color:#fff;font-size:9px;text-align:center;line-height:13px;margin-right:6px;vertical-align:1px}
.num--light{background:#fff;color:var(--navy)}
.item-title{font-weight:700;color:var(--navy);font-size:12px;letter-spacing:.4px;margin-bottom:3px}
.footer{position:absolute;left:0;right:0;bottom:0;height:92px;padding:20px 20px 0;display:flex;background:var(--paper)}
.footer .col h4{color:var(--navy);font-size:12px;font-weight:600;margin-bottom:7px}
.footer .col p{font-size:11px;line-height:1.4}
.footer .col--phone{width:175px}
.footer .col--phone p{font-weight:700}
.footer .col--web{width:305px}
.footer .col--addr{flex:1}

/* front */
.brand{position:absolute;left:20px;top:22px;display:flex;align-items:center;gap:8px}
.brand-mark{width:18px;height:18px;background:var(--navy)}
.brand-name{font-weight:800;color:var(--navy);font-size:17px;line-height:1.05;letter-spacing:.3px}
.hero-photo{position:absolute;left:245px;top:0;width:455px;height:302px;clip-path:polygon(80px 0,100% 0,100% 100%,0 100%);background:linear-gradient(135deg,#dfe6ee 0%,#b8c7d8 35%,#6c86a6 60%,#9c8068 82%,#3a3f52 100%)}
.about-band{position:absolute;left:0;top:122px;width:700px;height:180px;background:var(--navy);clip-path:polygon(0 0,340px 0,470px 100%,0 100%)}
.about{position:absolute;left:0;top:108px;width:350px}
.about .tab{margin-left:22px}
.about p{color:#fff;padding:8px 0 0 20px;width:330px;font-size:10.3px;line-height:1.2}
.why{position:absolute;left:20px;top:318px;width:660px}
.why-head{display:flex;align-items:center;background:var(--panel);height:30px}
.why-head .tab{height:30px;line-height:20px}
.why-lead{color:var(--navy);font-weight:600;font-size:12px;margin-left:12px}
.why p{font-size:10.8px}
.grid2{display:grid;grid-template-columns:1fr 1fr;column-gap:20px;row-gap:12px;margin-top:12px}
.process{position:absolute;left:0;top:598px;width:700px;height:300px;background:var(--navy);color:#fff}
.process .tab{position:absolute;top:-14px;left:22px}
.process .grid2{margin:30px 20px 0}
.process .item-title{color:#fff}
.bullets{list-style:none}
.bullets li{position:relative;padding-left:18px;margin-bottom:3px}
.bullets li::before{content:"";position:absolute;left:3px;top:4px;width:5px;height:5px;border-radius:50%;background:#fff}
.bullets li::after{content:"";position:absolute;left:5px;top:9px;width:1px;height:10px;background:#fff}
.bullets li:last-child::after{display:none}
.partner-strip{position:absolute;left:20px;top:250px;width:660px;height:36px;background:var(--paper);display:flex;align-items:center;justify-content:space-around;padding:0 10px}
.badge{height:16px;background:var(--line);border-radius:2px}
.sep{width:1px;height:22px;background:var(--navy)}

/* back */
.services{position:absolute;left:20px;top:20px;width:320px}
.services > p{margin-top:10px}
.quote{position:relative;background:var(--panel);padding:9px 12px 10px;margin:12px 0 16px}
.quote p{color:var(--navy)}
.quote .who{font-weight:700;margin-top:5px;font-size:10px}
.quote-mark{position:absolute;right:14px;bottom:-12px;color:var(--navy);font-weight:800;font-size:32px;line-height:1;letter-spacing:-4px}
.sub-title{color:var(--navy);font-weight:700;font-size:13.5px;margin:4px 0 3px}
.rings{list-style:none;margin-top:6px}
.rings li{position:relative;padding-left:16px;margin-bottom:6px}
.rings li strong{display:block;color:var(--navy);font-size:11.5px;font-weight:700;margin-bottom:1px}
.rings li::before{content:"";position:absolute;left:0;top:3px;width:7px;height:7px;border:2px solid var(--navy);border-radius:50%}
.right-col{position:absolute;left:360px;top:18px;width:320px}
.right-col .rings li{padding-left:18px}
.back-band{position:absolute;left:0;top:676px;width:700px;height:222px;background:var(--navy);clip-path:polygon(0 30px,340px 30px,345px 0,700px 0,700px 100%,0 100%)}
.carriers{position:absolute;left:20px;top:716px;width:320px;color:#fff}
.carriers h3{font-size:16px;font-weight:700;letter-spacing:1px;margin-bottom:7px}
.carriers ul{list-style:none;columns:2;column-gap:16px}
.carriers li{font-size:10px;font-weight:500;letter-spacing:.4px;padding-left:10px;position:relative;margin-bottom:1px}
.carriers li::before{content:"";position:absolute;left:0;top:4px;width:4px;height:4px;border-radius:50%;background:#fff}
.cta{margin-top:12px;background:var(--panel);padding:7px 12px;color:var(--navy);font-weight:700;font-size:11.5px;line-height:1.25}
.quote--float{position:absolute;left:360px;top:645px;width:310px;margin:0}
.updates{position:absolute;left:365px;top:722px;width:315px;color:#fff}
.updates .bullets li{margin-bottom:8px}
.updates .bullets li strong{display:block;font-size:11.5px;font-weight:700}
.updates .bullets li::after{height:30px}
</style>
</head>
<body>
<div class="sheet-row">

  <!-- Front side -->
  <section class="page page--front">
    <div class="brand">
      <div class="brand-mark"></div>
      <div class="brand-name">NORTHVALE<br>INSURANCE<br>NETWORK</div>
    </div>
    <div class="hero-photo" role="img" aria-label="Photo of a businessman working at a desk with a computer monitor showing a business insurance page"></div>
    <div class="about-band"></div>
    <div class="about">
      <span class="tab tab--light">ABOUT US</span>
      <p>Northvale Insurance Network is a full-service life insurance Brokerage General Agency (BGA) and serves financial advisors, independent insurance agents, and banks throughout the United States. Having served our customers for over 25 years, we are committed to helping financial advisors achieve their goals for their clients. Serving as a <b>one-stop shop for all life insurance solutions</b>, we offer a wide range of insurance products from multiple carriers, giving our advisors and agents access to a variety of options and solutions to meet their clients’ needs.</p>
    </div>

    <div class="why">
      <div class="why-head"><span class="tab">WHY NIN?</span><span class="why-lead">When you chose to work with NIN, you will add value to your firm overnight !</span></div>
      <div class="grid2">
        <div>
          <div class="item-title"><span class="num">1</span>Immediate Risk Management Partner</div>
          <p>We know insurance and understand your business. Your agents will <b>have access to a wide range of carriers, giving them options</b> to meet client needs. In addition, we only deal in insurance, so rest assured we leave the money management to you!</p>
        </div>
        <div>
          <div class="item-title"><span class="num">3</span>Customized Concierge Service</div>
          <p>This team of professionals leverage their experience and technology to <b>remove the pain points of writing policies</b>. Comprised of our licensing, application, and case management specialists, we handle every aspect of the process. No more application paperwork or underwriting hassle for your staff!</p>
        </div>
        <div>
          <div class="item-title"><span class="num">2</span>Experienced Insurance Specialists</div>
          <p>Our Point of Sales Specialists have many years of industry experience, hold various designations, and are licensed to provide a variety of products. These trained professionals <b>are located throughout the country</b> and are ready to provide prompt service to your staff.</p>
        </div>
        <div>
          <div class="item-title"><span class="num">4</span>Save Time and Money</div>
          <p>We have designed our services to operate efficiently, funded from the compensation we receive by the insurance carriers, meaning <b>no cost to you.</b> Our goal is to increase your production, while eliminating your internal salaries and benefits dedicated to insurance support.</p>
        </div>
      </div>
    </div>

    <div class="process">
      <span class="tab tab--light">OUR PROCESS</span>
      <div class="grid2">
        <div>
          <div class="item-title"><span class="num num--light">1</span>Quotes &amp; Analysis</div>
          <ul class="bullets">
            <li>Access to multiple carriers, including most industry leaders.</li>
            <li>Submit quotes online or simply email our staff.</li>
            <li>Consult our Specialists to find the best solution for your client.</li>
          </ul>
          <div class="item-title" style="margin-top:10px"><span class="num num--light">2</span>Licensing &amp; Appointment</div>
          <ul class="bullets">
            <li>Confirm agent license and appointment is up to date.</li>
            <li>If necessary, use our assistance to get appointed in a timely manner.</li>
            <li>Electronic signatures make the appointment process fast and easy.</li>
          </ul>
        </div>
        <div>
          <div class="item-title"><span class="num num--light">3</span>Applications &amp; Underwriting</div>
          <ul class="bullets">
            <li>Our specialists oversee the entire application and underwriting process.</li>
            <li>Direct contact with the client, ensuring confidential and private medical history conversation.</li>
            <li>Utilize technology to provide electronic signatures where possible.</li>
          </ul>
          <div class="item-title" style="margin-top:10px"><span class="num num--light">4</span>Policy Delivery &amp; Payout</div>
          <ul class="bullets">
            <li>Ensure policy documents are delivered in full and on time.</li>
            <li>Confirm premiums are paid and policies are in force.</li>
            <li>Facilitate payout for all of your policies.</li>
          </ul>
        </div>
      </div>
      <div class="partner-strip" aria-label="Partner carrier badges">
        <div class="badge" style="width:70px"></div><div class="sep"></div>
        <div class="badge" style="width:80px"></div><div class="sep"></div>
        <div class="badge" style="width:70px"></div><div class="sep"></div>
        <div class="badge" style="width:50px"></div><div class="sep"></div>
        <div class="badge" style="width:45px"></div><div class="sep"></div>
        <div class="badge" style="width:75px"></div>
      </div>
    </div>

    <footer class="footer">
      <div class="col col--phone"><h4>Phone</h4><p>555-210-4830<br>1-800-555-0172</p></div>
      <div class="col col--web"><h4>Email | website</h4><p>hello@<b>northvale-network</b>.com<br>www.<b>northvalenetwork</b>.com</p></div>
      <div class="col col--addr"><h4>Address</h4><p>820 Cedar Ridge Drive,<br>Suite 210 Fairview, OH 44126</p></div>
    </footer>
  </section>

  <!-- Back side -->
  <section class="page page--back">
    <div class="back-band"></div>
    <div class="services">
      <span class="tab">OUR SERVICES</span>
      <p>As a BGA, our mission is to connect agents and advisors with insurance carriers and help our customers find the correct product that meets each client’s needs. From our experienced Point of Sale Strategists to our professional Concierge Service Team, we provide value every step of the way, at no additional cost!</p>
      <div class="quote">
        <p>From quote to issue and review to service, each case is an opportunity of quality care.</p>
        <p class="who">Dana P, New Business Specialist -</p>
        <span class="quote-mark">”</span>
      </div>
      <div class="sub-title">Our Point of Sale Strategists</div>
      <p>Work directly with agents and advisors to provide experienced assistance for immediate client needs, as well as maximizing insurance planning to find opportunities for all clients.</p>
      <ul class="rings">
        <li><strong>Dedicated Strategists</strong>We develop a personal relationship with each advisor, giving you confidence that we are working in your best interest. Always here to help with quotes and analysis.</li>
        <li><strong>Quotes Made Easy</strong>Access our online system or simply email your specialist to receive quotes for your client reviews, life event circumstances, estate needs, or prospect meetings.</li>
        <li><strong>National Footprint</strong>Our team is nationwide, allowing us to serve you regardless of location, time zone, or licensing limitations.</li>
      </ul>
      <div class="sub-title" style="margin-top:10px">Our Concierge Service Team</div>
      <p>Is comprised of several specialists. Once an agent moves forward with an application, simply hand it off to our staff, ensuring your policy is processed accurately and delivered in a timely manner.</p>
      <div class="quote">
        <p>We are the go-to-person for anything the agent needs; we handle everything from A to Z!</p>
        <p class="who">Renee K, Application Specialist/Case Manager -</p>
        <span class="quote-mark">”</span>
      </div>
    </div>

    <div class="right-col">
      <ul class="rings">
        <li><strong>Dedicated Case Managers</strong>Your personal case manager gives us a better understanding of your business, expectations, and preferred process.</li>
        <li><strong>Carrier Familiarity</strong>Our experience enables us to provide correct forms from the get-go, as well as properly relay carrier specific processes &amp; manage expectations.</li>
        <li><strong>Agent Licensing</strong>We confirm you are correctly licensed &amp; appointed before applications are initiated. If appointment is needed, we help you get this done in a timely, technology efficient manner.</li>
        <li><strong>No Hassle Paperwork</strong>Our team will handle all application and under writing needs, assuring a efficient process &amp; less hassle for the agent.</li>
        <li><strong>No Fluff Process</strong>We create a seamless process by gathering what is required for underwriting, eliminating the need for unnecessary back and forth with clients that often delays the policy and annoys clients.</li>
      </ul>
      <div class="quote" style="margin-top:12px">
        <p>Oftentimes clients can be uncomfortable disclosing personal health history to their advisor, but will answer freely with someone in my role. I let clients know we have their best interest at heart.</p>
        <p class="who">Tamsin L, Application Specialist -</p>
        <span class="quote-mark">”</span>
      </div>
      <ul class="rings">
        <li><strong>Client Confidentiality</strong>Our application specialist contacts the client and takes the application, eliminating the need for clients to share personal medical information with their advisor.</li>
        <li><strong>Proactive Approach</strong>We proactively order medical records and exams for most cases, speeding up the UW process by days if not weeks, resulting in quicker decisions.</li>
        <li><strong>Electronic Signatures</strong>By leveraging technology, we will utilize electronic signature capabilities for both agent and client, speeding up the overall process.</li>
      </ul>
    </div>

    <div class="quote quote--float">
      <p>Our weekly updates keep advisors well informed throughout the process.</p>
      <p class="who">Marisa J, Senior Case Manager -</p>
      <span class="quote-mark">”</span>
    </div>

    <div class="carriers">
      <h3>LIST OF CARRIERS INCLUDE</h3>
      <ul>
        <li>SUMMIT MUTUAL</li><li>ORION LIFE</li><li>BEACON TRUST</li><li>HARBOR LIFE</li><li>KEYSTONE MUTUAL</li><li>PLAINS MUTUAL</li>
        <li>CRESTLINE</li><li>HUDSON LIFE</li><li>WESTSHORE LIFE</li><li>MERIDIAN</li><li>BASTION LIFE</li><li>GRANITE ASSURANCE</li>
      </ul>
      <div class="cta">We look forward to using our expertise<br>to help you grow your business.</div>
    </div>

    <div class="updates">
      <ul class="bullets">
        <li><strong>Recurring Updates</strong>Your case manager will keep you updated on the status of all cases.</li>
        <li><strong>Online Case Tracker</strong>This tool allows you to access the status of your cases. All carriers. All cases. All the time.</li>
        <li><strong>Policy Delivery</strong>We ensure premiums are paid and policy documents are delivered.</li>
      </ul>
    </div>

    <footer class="footer">
      <div class="col col--phone"><h4>Phone</h4><p>555-210-4830<br>1-800-555-0172</p></div>
      <div class="col col--web"><h4>Email | website</h4><p>hello@<b>northvale-network</b>.com<br>www.<b>northvalenetwork</b>.com</p></div>
      <div class="col col--addr"><h4>Address</h4><p>820 Cedar Ridge Drive,<br>Suite 210 Fairview, OH 44126</p></div>
    </footer>
  </section>

</div>
</body>
</html>
```